Restaurant needs take out menu design

I need a takeout menu design for a new restaurant. We will be printing via inkharbor.com. On their website, you can download blank templates.

See specs:
1. 11x17 accordion folding. http://www.inkharbor.com/take-out-menu-printing.html
2. Font is Times New Roman
3. All design/font on the menu will be black

*See menu inspiration attached. Feel free to reuse similar boarders and design.
*Attached is our logo
*Please let me know if any other information is needed.
*Attached is a our menu with prices.
*Please send to me in an ai file.

Industry/Entity Type

Restaurant

Font styles to use
Serif
Decorative

Requirements
Must have
• new times roman. black lettering
• all uppercase lettering
• must be in adobe illustrator format
• have the same feel as the menus I attached
Nice to have
• Leave the area for the telephone numbers, hours, address and business hours the same as the copy and pasted menu.
Should not have
• No other color than black

```html
<!DOCTYPE html>
<html lang="en">
<head>
<meta charset="utf-8">
<title>The Jade Court – Take Out Menu</title>
<link href="https://fonts.googleapis.com/css2?family=Tinos:ital,wght@0,400;0,700;1,400&display=swap" rel="stylesheet">
<style>
:root{
  --ink:#000;
  --sheet:#2b2b2b;
  --paper:#fff;
  --chili:#c8261d;
  --page:#fff;
}
*{box-sizing:border-box;margin:0;padding:0}
html,body{width:1200px;height:1200px;overflow:hidden;background:var(--page)}
body{position:relative;font-family:"Tinos","Times New Roman",serif;color:var(--ink);text-transform:uppercase}
.sheet{position:absolute;background:var(--sheet)}
.sheet--outside{left:209px;top:27px;width:763px;height:553px}
.sheet--inside{left:206px;top:628px;width:768px;height:544px}
.panel{position:absolute;background:var(--paper);border-radius:6px}
.panel::before{content:"";position:absolute;inset:4px;border:1.5px solid var(--ink);border-radius:5px}
.panel::after{content:"";position:absolute;inset:7px;border:0.6px solid var(--ink);border-radius:3px}
.panel > *{position:absolute;z-index:1}
.orn{background:radial-gradient(ellipse at center,#111 0%,#555 35%,rgba(255,255,255,0) 70%)}
.panel > .brand{z-index:2}
.brand{text-align:center;line-height:1;letter-spacing:.08em}
.brand .the,.brand .sub{display:block;font-size:.32em;letter-spacing:.5em}
.brand .main{display:block;font-size:1em}
.mini-brand{font-size:14px;background:var(--paper);padding:2px 0;border-radius:3px}
.band{background:var(--ink);color:var(--paper);font-size:7px;letter-spacing:.03em;height:11px;line-height:11px;padding:0 6px;border-radius:0 6px 6px 0;white-space:nowrap;overflow:visible}
.band--right{border-radius:6px 0 0 6px;text-align:right}
.band--center{border-radius:6px;text-align:center;font-size:9px;height:16px;line-height:16px}
.list{font-size:5.2px;line-height:6.5px}
.row{display:flex;justify-content:space-between;gap:4px;white-space:nowrap}
.row .p{flex:none}
.desc{font-style:italic;font-size:3.6px;line-height:4.4px;display:block;white-space:normal;letter-spacing:.02em}
.hot{display:inline-block;width:4px;height:2px;border-radius:2px 0 2px 0;background:var(--chili);margin-right:1px;vertical-align:middle}
.cols{display:flex;justify-content:flex-end;gap:12px;font-size:4.6px}
/* cover */
.cover .brand{left:20px;right:20px;top:86px;font-size:36px}
.menu-word{left:0;right:0;top:240px;text-align:center;font-size:44px;text-transform:none}
.contact{left:22px;right:18px;font-size:10px;text-transform:none;white-space:nowrap;overflow:hidden}
.lunch-intro{left:40px;right:40px;top:86px;text-align:center;font-style:italic;font-size:4.6px;line-height:5.6px}
.note{left:40px;right:30px;top:461px;text-align:center;font-size:6.6px;line-height:9px}
.happy{font-size:9px;font-weight:700;letter-spacing:.05em}
</style>
</head>
<body>

<section class="sheet sheet--outside">
  <div class="panel cover" style="left:15px;top:17px;width:170px;height:520px">
    <div class="orn" role="img" aria-label="Ornamental flourish" style="left:35px;top:16px;width:100px;height:36px"></div>
    <div class="brand"><span class="the">THE</span><span class="main">JADE</span><span class="sub">COURT</span></div>
    <div class="orn" role="img" aria-label="Ornamental chandelier flourish" style="left:42px;top:178px;width:86px;height:46px"></div>
    <div class="menu-word">Menu</div>
    <div class="orn" role="img" aria-label="Small scroll divider" style="left:38px;top:290px;width:94px;height:10px"></div>
    <div class="contact" style="top:330px;left:50px">Tel:......................</div>
    <div class="contact" style="top:347px;left:60px">......................</div>
    <div class="contact" style="top:362px;left:55px">Fax:......................</div>
    <div class="contact" style="top:382px">Website:.............................</div>
    <div class="contact" style="top:424px">Add:...........................................</div>
    <div class="contact" style="top:440px">...............................................</div>
    <div class="orn" role="img" aria-label="Ornamental flourish" style="left:35px;top:466px;width:100px;height:40px"></div>
  </div>

  <div class="panel" style="left:217px;top:17px;width:331px;height:520px">
    <div class="orn" role="img" aria-label="Corner flourish" style="left:12px;top:12px;width:30px;height:30px"></div>
    <div class="orn" role="img" aria-label="Corner flourish" style="right:12px;top:12px;width:30px;height:30px"></div>
    <div class="orn" role="img" aria-label="Corner flourish" style="left:12px;bottom:12px;width:30px;height:30px"></div>
    <div class="orn" role="img" aria-label="Corner flourish" style="right:12px;bottom:12px;width:30px;height:30px"></div>
    <div class="brand mini-brand" style="left:130px;width:72px;top:16px"><span class="the">THE</span><span class="main">JADE</span><span class="sub">COURT</span></div>
    <div class="band band--center" style="left:106px;width:122px;top:70px">LUNCH SPECIALS</div>
    <div class="lunch-intro">SERVED FROM 11:30 AM – 3:00PM MONDAY – FRIDAY (EXCLUDING HOLIDAYS)<br>WITH A CHOICE OF SOUP: WONTON, EGG DROP, OR HOT &amp; SOUR SOUP (EXCEPT NOODLE SOUP)<br>WITH A CHOICE OF RICE: WHITE RICE, BROWN RICE, OR VEGETABLE FRIED RICE<br>EGG ROLL OR SHRIMP ROLL $2.00 EXTRA</div>
    <div class="orn" role="img" aria-label="Ornamental chandelier flourish" style="left:125px;top:118px;width:82px;height:36px"></div>

    <div class="band" style="left:6px;width:62px;top:144px">$8.75</div>
    <div class="list" style="left:17px;top:158px;width:175px">
      <div>BEAN CURD WITH MIXED VEGETABLES</div>
      <div>SAUTEED MIXED VEGETABLES</div>
      <div><span class="hot"></span>BROCCOLI IN GARLIC SAUCE</div>
      <div>DRIED SAUTEED STRING BEANS</div>
      <div>LO MEIN WITH ROAST PORK, CHICKEN, BEEF, OR SHRIMP</div>
      <div>CHOW MEIN WITH ROAST PORK, CHICKEN, BEEF, OR SHRIMP</div>
    </div>
    <div class="band band--right" style="left:263px;width:62px;top:144px">$10.95</div>
    <div class="list" style="left:200px;top:158px;width:120px">
      <div>JUMBO SHRIMP WITH BROCCOLI</div>
      <div>JUMBO SHRIMP WITH MIXED VEGETABLES</div>
      <div>SHRIMP WITH LOBSTER SAUCE</div>
      <div><span class="hot"></span>KUNG PO SHRIMP WITH PEANUTS</div>
      <div>SAUTEED TWO DELICACIES</div>
      <div>SCALLOP WITH MIXED VEGETABLES</div>
      <div><span class="hot"></span>SCALLOPS WITH GARLIC SAUCE</div>
    </div>

    <div class="band" style="left:6px;width:62px;top:207px">$8.95</div>
    <div class="list" style="left:17px;top:221px;width:175px">
      <div>CHICKEN, BEEF, PORK, OR BABY SHRIMP</div>
      <div>WITH A CHOICE OF BROCCOLI, STRING BEANS, OR MIXED</div>
      <div>VEGETABLES AND A CHOICE OF BROWN SAUCE,</div>
      <div><span class="hot"></span>GARLIC SAUCE, BLACK BEAN SAUCE OR WHITE SAUCE</div>
      <div>&nbsp;</div>
      <div>SWEET &amp; SOUR CHICKEN OR PORK</div>
      <div>PEPPER STEAK WITH ONIONS</div>
      <div><span class="hot"></span>SAUTEED SHREDDED BEEF WITH HOT SAUCE</div>
      <div>CHICKEN WITH CASHEW NUTS</div>
    </div>
    <div class="band band--right" style="left:263px;width:62px;top:212px">$11.50</div>
    <div class="list" style="left:200px;top:233px;width:120px">
      <div>CRISPY SHRIMP</div>
      <div><span class="hot"></span>GENERAL TSO'S SHRIMP</div>
      <div><span class="hot"></span>HUNAN SHRIMP WITH WALNUTS</div>
      <div>GOLDEN ORANGE SHRIMP</div>
      <div><span class="hot"></span>SEAFOOD SUPREME</div>
      <div>HAPPY FAMILY</div>
      <div><span class="hot"></span>GENERAL TSO'S TRIPLE FRAGRANCE</div>
    </div>

    <div class="band" style="left:6px;width:62px;top:290px">$9.25</div>
    <div class="list" style="left:17px;top:306px;width:150px">
      <div>SESAME CHICKEN</div>
      <div><span class="hot"></span>GENERAL TSO'S CHICKEN</div>
      <div><span class="hot"></span>TANGERINE CHICKEN</div>
      <div>GOLDEN ORANGE CHICKEN</div>
      <div>SESAME BEEF</div>
      <div><span class="hot"></span>TANGERINE BEEF</div>
      <div>PEKING PORK CHOPS</div>
      <div><span class="hot"></span>MANDARIN PORK CHOPS</div>
      <div><span class="hot"></span>TRIPLE CROWN</div>
      <div><span class="hot"></span>BEEF NOODLE SOUP</div>
      <div>PORK CHOP NOODLE SOUP</div>
      <div>TEN INGREDIENTS NOODLE SOUP<span class="desc">(CHICKEN, PORK, SHRIMP AND MIXED VEGETABLES IN A CHICKEN BROTH)</span></div>
      <div><span class="hot"></span>DAN DAN NOODLES (PEANUT SESAME NOODLES)</div>
      <div><span class="hot"></span>PEKING NOODLES<span class="desc">(MINCED PORK, BEAN CURD, AND BAMBOO IN A BROWN HOISIN SAUCE)</span></div>
    </div>

    <div class="orn" role="img" aria-label="Flourished circle badge reading Happy Time" style="left:150px;top:316px;width:128px;height:128px"></div>
    <div class="happy" style="left:140px;top:372px;transform:rotate(35deg)">HAPPY TIME</div>

    <div class="note">WE CAN ALTER THE SPICINESS ACCORDING TO YOUR TASTE<br>CRISPY NOODLES ONLY COME WITH SOUP OR SHOW MEIN<br>ADDITIONAL SAUCE ON THE SIDE- EXTRA CHARGE $2.00</div>
  </div>

  <div class="panel" style="left:571px;top:17px;width:177px;height:520px">
    <div class="orn" role="img" aria-label="Ornamental flourish" style="left:74px;top:18px;width:84px;height:36px"></div>
    <div class="brand mini-brand" style="left:16px;width:56px;top:22px"><span class="the">THE</span><span class="main">JADE</span><span class="sub">COURT</span></div>

    <div class="band" style="left:6px;width:80px;top:79px">VEGETABLES</div>
    <div class="list" style="left:17px;top:92px;width:136px">
      <div>FILLER 1- TBD</div><div>FILLER 2- TBD</div><div>FILLER 3- TBD</div><div>FILLER 4- TBD</div><div>FILLER 5 -TBD</div>
      <div class="row"><span>MOO SHU VEGETABLES</span><span class="p">11.95</span></div>
      <div>DRIED SAUTEED STRING BEANS 11.95</div>
      <div class="row"><span><span class="hot"></span>SAUTEED BROCCOLI IN GARLIC SAUCE</span><span class="p">11.95</span></div>
      <div class="row"><span><span class="hot"></span>EGGPLANT IN GARLIC SAUCE</span><span class="p">11.95</span></div>
      <div class="row"><span>MIXED VEGETABLES IN BROWN SAUCE</span><span class="p">11.95</span></div>
      <div class="row"><span>EVER GREEN IN LIGHT FRESH GARLIC SAUCE</span><span class="p">11.95</span></div>
      <div><span class="desc">(BROCCOLI, STRING BEANS, ASPARAGUS AND SNOW PEAS)</span></div>
      <div class="row"><span>SAUTEED SHANGHAI BOK CHOY</span><span class="p">11.95</span></div>
      <div class="row"><span>BEAN CURD WITH MIXED VEGETABLES</span><span class="p">12.75</span></div>
      <div class="row"><span><span class="hot"></span>GENERAL TSO'S BEAN CURD</span><span class="p">12.95</span></div>
    </div>

    <div class="band" style="left:6px;width:80px;top:207px">SIDE ORDERS</div>
    <div class="cols" style="left:17px;width:136px;top:218px"><span>PT.</span><span>QT.</span></div>
    <div class="list" style="left:17px;top:226px;width:136px">
      <div>PANCAKE (1) .50</div>
      <div>FRESH CRISPY NOODLES 1.50</div>
      <div>CANNED SODA 1.50</div>
      <div class="row"><span>WHITE RICE</span><span class="p">1.75 &nbsp;&nbsp; 3.00</span></div>
      <div class="row"><span>BROWN RICE</span><span class="p">2.25 &nbsp;&nbsp; 4.00</span></div>
      <div>&nbsp;</div>
      <div class="row"><span>FRIED RICE <i>(CHICKEN, PORK, OR VEG)</i></span><span class="p">6.95 &nbsp;&nbsp; 8.95</span></div>
      <div class="row"><span>FRIED RICE <i>(BEEF OR SHRIMP)</i></span><span class="p">7.95 &nbsp;&nbsp; 9.95</span></div>
      <div class="row"><span>HOUSE SPECIAL FRIED RICE</span><span class="p">8.95 &nbsp;&nbsp; 9.95</span></div>
      <div>**BROWN RICE AVAILABLE UPON</div>
      <div class="row"><span>REQUEST FOR AN EXTRA CHARGE</span><span class="p">1.00 &nbsp;&nbsp;&nbsp;&nbsp;&nbsp;&nbsp;&nbsp;&nbsp;</span></div>
      <div>&nbsp;</div>
      <div class="row"><span>LO MEIN <i>(CHICKEN, PORK, OR VEG)</i></span><span class="p">7.95 &nbsp;&nbsp; 9.95</span></div>
      <div class="row"><span>LO MEIN <i>(BEEF OR SHRIMP)</i></span><span class="p">8.95 &nbsp; 10.95</span></div>
      <div class="row"><span>HOUSE SPECIAL LO MEIN</span><span class="p">10.50 &nbsp; 12.50</span></div>
      <div>CHOW MEIN<span class="desc">(CHICKEN, PORK, BEEF, SHRIMP, VEGETABLE, OR HOUSE) 9.95</span></div>
      <div>CHOW FUN NOODLES<span class="desc">(CHICKEN, PORK, BEEF, SHRIMP, VEGETABLE, OR HOUSE) 9.95</span></div>
      <div>MEI FUN NOODLES<span class="desc">(CHICKEN, PORK, BEEF, SHRIMP, VEGETABLE, OR HOUSE) 9.95</span></div>
      <div class="row"><span>CURRY MEI FUN SINGAPORE STYLE WITH EGG</span><span class="p">12.95</span></div>
      <div class="row"><span>CANTONESE PAN FRIED NOODLES</span><span class="p">16.95</span></div>
    </div>

    <div class="band" style="left:6px;width:80px;top:402px">APPETIZERS</div>
    <div class="list" style="left:17px;top:416px;width:136px">
      <div class="row"><span>CHILLED SEAWEED IN SEASONED GARLIC</span><span class="p">4.50</span></div>
      <div class="row"><span>CHILLED SWEET CABBAGE</span><span class="p">4.50</span></div>
      <div class="row"><span>FRESH CUCUMBER IN SEASONED GARLIC</span><span class="p">4.95</span></div>
      <div class="row"><span><span class="hot"></span>DAN DAN NOODLE</span><span class="p">6.50</span></div>
      <div><span class="desc">(EGG NOODLES IN OUR HOUSE PEANUT SESAME SAUCE)</span></div>
      <div>BEEF TENDON AND TRIPE IN A HOT</div>
      <div class="row"><span><span class="hot"></span>SZECHUAN PEPPER SAUCE</span><span class="p">7.95</span></div>
      <div class="row"><span><span class="hot"></span>BANG BANG CHICKEN</span><span class="p">7.95</span></div>
      <div><span class="desc">(SHREDDED CHICKEN WITH A HOT PEANUT SESAME SAUCE, SERVED CHILLED)</span></div>
      <div class="row"><span><span class="hot"></span>SPICY SHRIMP IN HOT OIL</span><span class="p">7.95</span></div>
    </div>
  </div>
</section>

<section class="sheet sheet--inside">
  <div class="panel" style="left:16px;top:16px;width:172px;height:512px">
    <div class="orn" role="img" aria-label="Ornamental flourish" style="left:72px;top:14px;width:82px;height:34px"></div>
    <div class="brand mini-brand" style="left:18px;width:52px;top:18px"><span class="the">THE</span><span class="main">JADE</span><span class="sub">COURT</span></div>

    <div class="band" style="left:6px;width:80px;top:70px">SOUPS</div>
    <div class="cols" style="left:17px;width:136px;top:80px"><span>PT.</span><span>QT.</span></div>
    <div class="list" style="left:17px;top:86px;width:136px">
      <div class="row"><span>EGG DROP SOUP</span><span class="p">2.75 &nbsp; 4.95</span></div>
      <div class="row"><span><span class="hot"></span>HOT &amp; SOUR SOUP &nbsp;&nbsp; 3.95</span><span class="p">6.75</span></div>
      <div class="row"><span>WONTON SOUP</span><span class="p">3.95 &nbsp; 6.75</span></div>
      <div class="row"><span>BEAN CURD SOUP WITH VEGETABLES (2)</span><span class="p">6.95 &nbsp;&nbsp;&nbsp;&nbsp;&nbsp;&nbsp;&nbsp;</span></div>
      <div class="row"><span>CHICKEN CORN SOUP (2)</span><span class="p">7.95</span></div>
      <div class="row"><span>TEN INGREDIENTS RICE SOUP (2)</span><span class="p">7.95 &nbsp;&nbsp;&nbsp;&nbsp;&nbsp;&nbsp;&nbsp;</span></div>
      <div class="row"><span>SYMPHONY SEAFOOD SOUP (FOR 2)</span><span class="p">12.95 &nbsp;&nbsp;&nbsp;&nbsp;&nbsp;&nbsp;&nbsp;</span></div>
    </div>

    <div class="band" style="left:6px;width:80px;top:138px">APPETIZERS</div>
    <div class="list" style="left:17px;top:152px;width:136px;line-height:6.3px">
      <div class="row"><span>VEGETABLE ROLL</span><span class="p">2.25</span></div>
      <div class="row"><span>EGG ROLL</span><span class="p">2.50</span></div>
      <div class="row"><span>SHRIMP ROLL</span><span class="p">2.50</span></div>
      <div class="row"><span>STEAMED EDAMAME</span><span class="p">3.95</span></div>
      <div class="row"><span>SCALLION PANCAKES</span><span class="p">4.50</span></div>
      <div class="row"><span><span class="hot"></span>COLD NOODLES IN SESAME SAUCE</span><span class="p">4.95</span></div>
      <div class="row"><span>CRISPY CRAB RAGOON (5)</span><span class="p">4.95</span></div>
      <div class="row"><span>SHRIMP TOAST (4)</span><span class="p">5.75</span></div>
      <div class="row"><span>BARBECUED BEEF STICKS (2)</span><span class="p">5.95</span></div>
      <div class="row"><span>STEAMED DUMPLINGS (6)</span><span class="p">6.50</span></div>
      <div class="row"><span>PAN FRIED DUMPLINGS (6)</span><span class="p">6.50</span></div>
      <div class="row"><span><span class="hot"></span>DUMPLINGS WITH HOT OIL</span><span class="p">&nbsp;</span></div>
      <div class="row"><span><i>(PEANUT SESAME SAUCE) (6)</i></span><span class="p">6.50</span></div>
      <div class="row"><span><span class="hot"></span>SPICY CHICKEN DUMPLINGS (10)</span><span class="p">6.50</span></div>
      <div class="row"><span>STEAMED EDAMAME DUMPLINGS (6)</span><span class="p">6.50</span></div>
      <div class="row"><span>STEAMED SHRIMP DUMPLINGS (4)</span><span class="p">6.50</span></div>
      <div class="row"><span>SIU MAI DUMPLINGS (4)</span><span class="p">6.50</span></div>
      <div class="row"><span>VEGETABLE DUMPLINGS (6)</span><span class="p">6.50</span></div>
      <div>THREE KINDS OF DUMPLINGS</div>
      <div class="row"><span><i>(PORK, VEGETABLE, AND SHRIMP)</i></span><span class="p">6.95</span></div>
      <div class="row"><span>BONELESS RIBS</span><span class="p">7.95</span></div>
      <div class="row"><span>BACON SHRIMP ROLLS (6)</span><span class="p">8.50</span></div>
      <div class="row"><span>BARBECUED SPARE RIBS</span><span class="p">(4) 9.95 (8) 15.95</span></div>
      <div class="row"><span>PU PU PLATTER (FOR 2)</span><span class="p">16.95 &nbsp;&nbsp;&nbsp;&nbsp;&nbsp;&nbsp;&nbsp;</span></div>
      <div>SHRIMP TOAST, BBQ SPARE RIBS, BEEF STICKS, SHRIMP</div>
      <div>ROLLS, SIU MAI DUMPLINGS, AND FRIED DUMPLINGS</div>
    </div>

    <div class="band" style="left:6px;width:80px;top:332px">CHICKENS</div>
    <div class="list" style="left:17px;top:347px;width:136px">
      <div class="row"><span>MOO SHU CHICKEN</span><span class="p">13.50</span></div>
      <div class="row"><span>CHICKEN WITH BROCCOLI</span><span class="p">13.50</span></div>
      <div class="row"><span>CHICKEN WITH MIXED VEGETABLES</span><span class="p">13.50</span></div>
      <div class="row"><span>CHICKEN WITH CASHEW NUTS</span><span class="p">13.50</span></div>
      <div class="row"><span><span class="hot"></span>KUNG PO CHICKEN WITH PEANUTS</span><span class="p">13.50</span></div>
      <div class="row"><span><span class="hot"></span>CHICKEN IN GARLIC SAUCE</span><span class="p">13.50</span></div>
      <div class="row"><span>CHICKEN WITH STRING BEANS</span><span class="p">13.50</span></div>
      <div class="row"><span>SWEET &amp; SOUR CHICKEN</span><span class="p">13.50</span></div>
      <div class="row"><span>CHICKEN WITH EGGPLANT</span><span class="p">13.95</span></div>
      <div class="row"><span><span class="hot"></span>HUNAN CHICKEN WITH BLACK BEAN SAUCE</span><span class="p">13.95</span></div>
      <div class="row"><span>CHICKEN WITH SNOW PEAS</span><span class="p">13.95</span></div>
      <div class="row"><span>CHICKEN WITH ASPARAGUS</span><span class="p">13.95</span></div>
      <div class="row"><span><span class="hot"></span>PEPPERCORN CHICKEN</span><span class="p">13.95</span></div>
    </div>

    <div class="band" style="left:6px;width:80px;top:444px">PORK</div>
    <div class="list" style="left:17px;top:458px;width:136px">
      <div class="row"><span>SWEET &amp; SOUR PORK</span><span class="p">12.95</span></div>
      <div class="row"><span><span class="hot"></span>PORK IN GARLIC SAUCE</span><span class="p">12.95</span></div>
      <div class="row"><span>SLICED PORK WITH MIXED VEGETABLES</span><span class="p">12.95</span></div>
      <div class="row"><span>SLICED PORK WITH STRING BEANS</span><span class="p">12.95</span></div>
      <div class="row"><span>MOO SHU PORK</span><span class="p">12.95</span></div>
    </div>
  </div>

  <div class="panel" style="left:220px;top:16px;width:331px;height:512px">
    <div class="orn" role="img" aria-label="Corner flourish" style="left:16px;top:12px;width:34px;height:34px"></div>
    <div class="orn" role="img" aria-label="Corner flourish" style="right:16px;top:12px;width:34px;height:34px"></div>
    <div class="orn" role="img" aria-label="Ornamental flourish, left" style="left:90px;top:20px;width:46px;height:26px"></div>
    <div class="orn" role="img" aria-label="Ornamental flourish, right" style="left:196px;top:20px;width:46px;height:26px"></div>
    <div class="brand mini-brand" style="left:138px;width:56px;top:18px"><span class="the">THE</span><span class="main">JADE</span><span class="sub">COURT</span></div>

    <div class="band" style="left:6px;width:90px;top:62px">HOUSE SPECIALTIES</div>
    <div class="list" style="left:13px;top:76px;width:300px;font-size:4.7px;line-height:5.1px">
      <div class="row"><span>BASIL CHICKEN</span><span class="p">15.50</span></div><span class="desc">CHUNKS OF DARK MEAT CHICKEN SAUTEED IN A DELICIOUS BASIL SAUCE WITH FRESH GINGER</span>
      <div class="row"><span>SESAME CHICKEN</span><span class="p">15.50</span></div><span class="desc">CRISPY CHUNKS OF CHICKEN IN A SWEET BROWN SAUCE WITH A SHOWER OF SESAME SEEDS</span>
      <div class="row"><span><span class="hot"></span>GENERAL TSO'S CHICKEN</span><span class="p">15.50</span></div><span class="desc">CRISPY CHICKEN SAUTEED IN OUR TANGY GENERAL TSO'S SAUCE</span>
      <div class="row"><span><span class="hot"></span>TANGERINE CHICKEN</span><span class="p">15.50</span></div><span class="desc">CRISPY CHUNKS OF CHICKEN SAUTEED IN A TANGERINE FLAVORED SPICY SAUCE</span>
      <div class="row"><span><span class="hot"></span>IMPERIAL CHICKEN</span><span class="p">15.50</span></div><span class="desc">CHUNKS OF CHICKEN, DRY SAUTEED WITH THREE KINDS OF HOT PEPPERS</span>
      <div class="row"><span>PEKING PORK CHOP</span><span class="p">16.95</span></div><span class="desc">MARINATED SLICES OF PORK CHOP LIGHTLY FRIED, THEN SAUTEED IN OUR TANGY SAUCE</span>
      <div class="row"><span><span class="hot"></span>MANDARIN PORK CHOP</span><span class="p">16.95</span></div><span class="desc">CRISPY SLICES OF PORK CHOP IN OUR SPECIAL SAUCE WITH FRESH SHREDDED SCALLIONS</span>
      <div class="row"><span>GOLDEN ORANGE CHICKEN</span><span class="p">16.95</span></div><span class="desc">CRISPY WHITE MEAT CHICKEN WITH FRESH FRUIT IN A SWEET GOLDEN SAUCE</span>
      <div class="row"><span><span class="hot"></span>SIZZLING TRIPLE DELIGHT</span><span class="p">17.95</span></div><span class="desc">SLICED BEEF, CHICKEN AND PORK WITH FRESH VEGETABLES SERVED ON A SIZZLING PLATTER</span>
      <div class="row"><span><span class="hot"></span>TRIPLE CROWN</span><span class="p">17.95</span></div><span class="desc">SLICED TENDERLOIN OF PORK, BEEF AND CHICKEN WITH VEGETABLES IN A SPICY GARLIC SAUCE</span>
      <div class="row"><span><span class="hot"></span>HUNAN LAMB</span><span class="p">17.95</span></div><span class="desc">SLICED LEG OF LAMB WITH WATER CHESTNUTS AND YELLOW PEPPERS IN A SPICY BLACK BEAN SAUCE</span>
      <div class="row"><span>MONGOLIAN LAMB</span><span class="p">17.95</span></div><span class="desc">SLICED LEG OF LAMB STIR FRIED WITH VEGETABLES IN A BROWN SAUCE</span>
      <div class="row"><span><span class="hot"></span>TANGERINE BEEF</span><span class="p">17.95</span></div><span class="desc">CRISPY CHUNKS OF STEAK SAUTEED IN A SPICY TANGERINE FLAVORED SAUCE</span>
      <div class="row"><span>SESAME BEEF</span><span class="p">17.95</span></div><span class="desc">CRISPY CHUNKS OF BEEF IN A SWEET BROWN SAUCE WITH SESAME SEEDS</span>
      <div class="row"><span>WU-XI RIBS</span><span class="p">17.95</span></div><span class="desc">TENDER PORK RIBS SAUTEED IN OUR SWEET AND TANGY SAUCE, SERVED ON A BED OF BOK CHOY</span>
      <div class="row"><span><span class="hot"></span>HUNAN DUCK</span><span class="p">19.95</span></div><span class="desc">CRISPY BONELESS DUCK TOPPED WITH MIXED VEGETABLES IN A SPICY HUNAN SAUCE</span>
      <div class="row"><span><span class="hot"></span>HUNAN SHRIMP WITH WALNUTS</span><span class="p">19.95</span></div><span class="desc">CRISPY SHRIMP SAUTEED IN A RED SPICY SAUCE WITH WALNUTS</span>
      <div class="row"><span><span class="hot"></span>GENERAL TSO'S SHRIMP</span><span class="p">19.95</span></div><span class="desc">CRISPY SHRIMP SAUTEED IN OUR TANGY GENERAL TSO'S SAUCE</span>
      <div class="row"><span><span class="hot"></span>TANGERINE SCALLOPS</span><span class="p">19.95</span></div><span class="desc">SUCCULENT JUMBO SCALLOPS IN A TANGERINE FLAVORED SPICY SAUCE WITH BROCCOLI</span>
      <div class="row"><span>LAKE TUNG TING DUET</span><span class="p">21.95</span></div><span class="desc">STIR-FRIED JUMBO SHRIMP AND SLICED CHICKEN WITH MIXED VEGETABLES IN A WHITE SAUCE</span>
      <div class="row"><span>HAPPY FAMILY</span><span class="p">21.95</span></div><span class="desc">SLICED PORK, BEEF, CHICKEN, SHRIMP AND SCALLOPS WITH VEGETABLES IN A BROWN SAUCE</span>
      <div class="row"><span>MONGOLIAN TRIPLE FEAST</span><span class="p">21.95</span></div><span class="desc">SLICED CHICKEN, BEEF AND JUMBO SHRIMP WITH SEASONED VEGETABLES IN OUR HOUSE SAUCE</span>
      <div class="row"><span><span class="hot"></span>GENERAL TSO'S TRIPLE FRAGRANCE</span><span class="p">21.95</span></div><span class="desc">CRISPY CHICKEN, BEEF AND SHRIMP WITH BABY CORN AND BROCCOLI IN OUR TANGY SAUCE</span>
      <div class="row"><span><span class="hot"></span>SEAFOOD SUPREME</span><span class="p">21.95</span></div><span class="desc">SHRIMP AND SCALLOPS WITH ASSORTED VEGETABLES IN GARLIC SAUCE</span>
      <div class="row"><span>GOLDEN ORANGE SHRIMP</span><span class="p">21.95</span></div><span class="desc">CRISPY JUMBO SHRIMP WITH FRESH FRUIT IN A SWEET GOLDEN SAUCE</span>
      <div class="row"><span>FILET MIGNON CHINESE STYLE</span><span class="p">22.95</span></div><span class="desc">TENDER FILET MIGNON WITH MUSHROOMS AND ONIONS SERVED IN OUR SWEET RED SAUCE</span>
      <div class="row"><span>GOLD COIN STEAK</span><span class="p">22.95</span></div><span class="desc">SLICED FILET MIGNON SAUTEED WITH FRESH VEGETABLES IN OUR DELICIOUS BROWN SAUCE</span>
      <div class="row"><span>VOLCANO STEAK</span><span class="p">22.95</span></div><span class="desc">SLICED FILET MIGNON WITH MUSHROOMS AND ONIONS IN OUR FLAMING RUM SAUCE</span>
      <div class="row"><span><span class="hot"></span>SIZZLING FILET MIGNON</span><span class="p">22.95</span></div><span class="desc">SLICED FILET MIGNON STIR-FRIED WITH ONIONS AND ASPARAGUS ON A SIZZLING PLATTER</span>
      <div class="row"><span>SEAFOOD DELIGHT IN BIRD'S NEST</span><span class="p">23.95</span></div><span class="desc">LOBSTER MEAT, SHRIMP AND SCALLOPS WITH VEGETABLES SERVED IN A CRISPY BASKET</span>
      <div class="row"><span>SEAFOOD COUNTRY STYLE</span><span class="p">23.95</span></div><span class="desc">LOBSTER MEAT, SHRIMP AND SCALLOPS WITH FRESH VEGETABLES IN A TANGY BROWN SAUCE</span>
      <div class="row"><span><span class="hot"></span>EMPIRE SEAFOOD COMBO</span><span class="p">23.95</span></div><span class="desc">JUMBO SHRIMP, SCALLOPS, LOBSTER AND VEGETABLES SAUTEED IN A SPICY SAUCE</span>
      <div class="row"><span>SAUTEED SEAFOOD COMBO</span><span class="p">23.95</span></div>
      <div>JUMBO SHRIMP, SCALLOP AND LOBSTER MEAT SAUTEED IN A LIGHT SCALLION SAUCE SERVED IN A HOT CHAFING</div>
      <div class="row"><span>DISH DRAGON &amp; PHOENIX</span><span class="p">29.95</span></div><span class="desc">LOBSTER MEAT AND SHRIMP IN A WHITE SAUCE ON ONE SIDE AND CRISPY CHICKEN IN BROWN SAUCE ON THE OTHER</span>
      <div class="row"><span>SURF &amp; TURF</span><span class="p">31.95</span></div><span class="desc">LOBSTER MEAT AND SHRIMP IN A WHITE SAUCE WITH SLICED FILET MIGNON IN BROWN SAUCE</span>
      <div class="row"><span>PEKING DUCK</span><span class="p">(HALF) 19.95 (WHOLE) 34.95</span></div><span class="desc">OVEN ROASTED DUCK CARVED AT YOUR TABLE AND SERVED WITH SCALLIONS, HOISIN SAUCE AND PANCAKES</span>
    </div>
  </div>

  <div class="panel" style="left:574px;top:16px;width:178px;height:512px">
    <div class="orn" role="img" aria-label="Ornamental flourish" style="left:24px;top:14px;width:82px;height:34px"></div>
    <div class="brand mini-brand" style="left:108px;width:52px;top:18px"><span class="the">THE</span><span class="main">JADE</span><span class="sub">COURT</span></div>

    <div class="band band--right" style="left:86px;width:86px;top:67px">BEEF</div>
    <div class="list" style="left:24px;top:82px;width:132px">
      <div class="row"><span>BEEF WITH BROCCOLI</span><span class="p">14.95</span></div>
      <div class="row"><span>BEEF WITH SNOW PEAS</span><span class="p">14.95</span></div>
      <div class="row"><span>PEPPER STEAK WITH ONIONS</span><span class="p">14.95</span></div>
      <div class="row"><span><span class="hot"></span>SAUTEED SHREDDED HOT BEEF</span><span class="p">14.95</span></div>
      <div class="row"><span>BEEF WITH MIXED VEGETABLES</span><span class="p">14.95</span></div>
      <div class="row"><span><span class="hot"></span>BEEF IN GARLIC SAUCE</span><span class="p">14.95</span></div>
      <div class="row"><span>BEEF WITH SCALLIONS</span><span class="p">14.95</span></div>
      <div class="row"><span>BEEF WITH ASPARAGUS</span><span class="p">14.95</span></div>
    </div>

    <div class="band band--right" style="left:86px;width:86px;top:150px">FISH</div>
    <div class="list" style="left:20px;top:164px;width:136px">
      <div class="row"><span>WHOLE FISH</span><span class="p" style="font-size:4px">MARKET PRICE</span></div>
      <div>STEAMED, CRISPY, <span class="hot"></span>HUNAN STYLE</div>
      <div>&nbsp;</div>
      <div class="row"><span>FLOUNDER DRAGON BOAT</span><span class="p" style="font-size:4px">MARKET PRICE</span></div>
      <div>SLICED FILET OF FLOUNDER</div>
      <div>SAUTEED WITH MIXED VEGETABLES</div>
      <div>IN A DELICATE GINGER SCALLION</div>
      <div>SAUCE SERVED OVER A CRISPY FISHBONE</div>
      <div>&nbsp;</div>
      <div class="row"><span>HEAVENLY FISH</span><span class="p" style="font-size:4px">MARKET PRICE</span></div>
      <div>STEAMED CHILEAN SEA BASS STEAK</div>
      <div>WITH A CHOICE OF GINGER SCALLION</div>
      <div>SAUCE OR BLACK BEAN SAUCE</div>
      <div>&nbsp;</div>
      <div class="row"><span>CRISPY CHILEAN SEA BASS</span><span class="p" style="font-size:4px">MARKET PRICE</span></div>
      <div>SERVED WITH FRESH SCALLIONS</div>
    </div>

    <div class="band band--right" style="left:86px;width:86px;top:278px">SEAFOOD</div>
    <div class="list" style="left:20px;top:294px;width:136px">
      <div class="row"><span>MOO SHU SHRIMP <i>(WITH 4 PANCAKES)</i></span><span class="p">15.95</span></div>
      <div class="row"><span>SHRIMP WITH BROCCOLI</span><span class="p">17.50</span></div>
      <div class="row"><span>SHRIMP WITH MIXED VEGETABLES</span><span class="p">17.50</span></div>
      <div class="row"><span>SHRIMP IN LOBSTER SAUCE</span><span class="p">17.50</span></div>
      <div class="row"><span>SHRIMP IN BLACK BEAN SAUCE</span><span class="p">17.50</span></div>
      <div class="row"><span><span class="hot"></span>SHRIMP IN GARLIC SAUCE</span><span class="p">17.50</span></div>
      <div class="row"><span><span class="hot"></span>KUNG PO SHRIMP WITH PEANUTS</span><span class="p">17.50</span></div>
      <div class="row"><span>SHRIMP WITH ASPARAGUS</span><span class="p">17.95</span></div>
      <div class="row"><span><span class="hot"></span>SCALLOPS IN GARLIC SAUCE</span><span class="p">17.95</span></div>
      <div class="row"><span>SCALLOPS WITH MIXED VEGETABLES</span><span class="p">17.95</span></div>
    </div>

    <div class="band band--right" style="left:86px;width:86px;top:378px">ENTREES</div>
    <div class="list" style="left:17px;top:392px;width:142px;line-height:6px">
      <div class="row"><span>SAUTEED RICE CAKE</span><span class="p">12.95</span></div>
      <span class="desc">(CHEWY RICE CAKE SAUTEED WITH BOK CHOY AND SHREDDED PORK)</span>
      <div class="row"><span><span class="hot"></span>"ANTS ON A TREE"</span><span class="p">12.95</span></div>
      <span class="desc">(CLEAR VERMICELLI NOODLES WITH MINCED PORK IN A SPICY SAUCE)</span>
      <div>SOFT BEAN CURD CASSEROLE IN BROWN SAUCE</div>
      <div class="row"><span>HOUSE BEAN CURD</span><span class="p">12.95</span></div>
      <div>BEAN CURD HUNAN STYLE WITH MINCED PORK</div>
      <div class="row"><span><i>(MA PO TOFU)</i></span><span class="p">12.95</span></div>
      <div class="row"><span><span class="hot"></span>SPICY BEEF WITH HOT PEPPERS</span><span class="p">15.95</span></div>
      <span class="desc">(SHREDDED BEEF WITH HOT CHILI PEPPERS)</span>
      <div class="row"><span><span class="hot"></span>SICHUAN BOILED STEW IN A FIRE HOT OIL SAUCE</span><span class="p">17.95</span></div>
      <span class="desc">(BEEF, CHICKEN, PORK OR FISH — A CLASSIC TONGUE-BURNING DISH)</span>
      <div class="row"><span>SALT PEPPER SHRIMP WITH SCALLIONS</span><span class="p">19.95</span></div>
      <div>SEA CUCUMBER 28.50</div>
      <span class="desc">(SAUTEED WITH VEGETABLES IN A BROWN SAUCE)</span>
    </div>
  </div>
</section>

</body>
</html>
```